New Year's Eve Wedding Save the Date

Lise and Marcus (we) are getting married 2016-12-31. I'm a hockey player, and she's into movies... we have 2 yellow labs, and we want a Save the Date postcard that matches our personality and the excitement of the event. See attached mock up that I've created (which will be what we fall back on if we can't find a design we like). I like the idea of the silhouette people and dogs under fireworks but am open to other concepts as well. String lights, champagne bottles/flutes, etc...

Industry/Entity Type

Wedding

Font styles to use
Script

```html
<!DOCTYPE html>
<html lang="en">
<head>
<meta charset="utf-8">
<title>Save the Date – Lise &amp; Marcus</title>
<link rel="stylesheet" href="https://fonts.googleapis.com/css2?family=Italianno&family=Old+Standard+TT:wght@400;700&family=Kanit:ital,wght@1,600&display=swap">
<style>
  :root {
    --paper: #fef8c0;
    --ink-brown: #3b1a14;
    --ink-olive: #5a4d2c;
    --ink-red: #b5252b;
    --ink-dark: #222222;
    --ink-black: #111111;
    --ornament-fill: #c9b98a;
  }
  html, body {
    margin: 0;
    padding: 0;
    overflow: hidden;
    background: var(--paper);
  }
  .postcard {
    position: relative;
    width: 1200px;
    height: 928px;
    background: var(--paper);
    overflow: hidden;
  }
  .postcard > * { position: absolute; margin: 0; }

  .ornament {
    background: var(--ornament-fill);
    border-radius: 22px;
    opacity: 0.55;
  }
  .ornament--header-left { left: 26px; top: 94px; width: 112px; height: 76px; }
  .ornament--header-right { left: 470px; top: 94px; width: 112px; height: 76px; }
  .ornament--divider { left: 226px; top: 440px; width: 178px; height: 42px; }
  .ornament--footer { left: 210px; top: 746px; width: 194px; height: 48px; }
  .ornament--spine { left: 582px; top: 378px; width: 44px; height: 178px; }

  .heading {
    left: 90px;
    width: 430px;
    top: 122px;
    text-align: center;
    font-family: "Old Standard TT", serif;
    font-weight: 700;
    font-size: 40px;
    letter-spacing: 5px;
    color: var(--ink-olive);
    line-height: 1;
  }
  .heading__the {
    font-family: "Italianno", cursive;
    font-weight: 400;
    font-size: 44px;
    letter-spacing: 0;
  }
  .couple {
    left: 30px;
    width: 560px;
    top: 165px;
    text-align: center;
    font-family: "Italianno", cursive;
    font-size: 118px;
    line-height: 1.1;
    color: var(--ink-red);
    white-space: nowrap;
  }
  .announce {
    left: 60px;
    width: 490px;
    text-align: center;
    font-family: "Old Standard TT", serif;
    font-weight: 700;
    color: var(--ink-olive);
    line-height: 1;
    letter-spacing: 4px;
  }
  .announce--line1 { top: 318px; font-size: 24px; }
  .announce--line2 { top: 348px; font-size: 24px; }
  .announce--on { top: 392px; font-size: 30px; }

  .rule {
    height: 3px;
    background: var(--ink-brown);
  }
  .rule--left { left: 32px; top: 464px; width: 170px; }
  .rule--right { left: 415px; top: 464px; width: 153px; }

  .date {
    left: 60px;
    width: 490px;
    top: 478px;
    text-align: center;
    font-family: "Kanit", sans-serif;
    font-style: italic;
    font-weight: 600;
    font-size: 60px;
    letter-spacing: 12px;
    color: var(--ink-dark);
    line-height: 1.1;
  }
  .about {
    left: 20px;
    width: 570px;
    top: 620px;
    text-align: center;
    font-family: "Old Standard TT", serif;
    font-weight: 700;
    font-size: 22px;
    line-height: 30px;
    letter-spacing: 4px;
    text-transform: uppercase;
    color: var(--ink-black);
  }

  .spine {
    width: 5px;
    left: 599px;
    background: var(--ink-brown);
  }
  .spine--top { top: 22px; height: 336px; }
  .spine--bottom { top: 577px; height: 340px; }

  .stamp-box {
    left: 964px;
    top: 85px;
    width: 160px;
    height: 160px;
    border: 4px solid #000;
    box-sizing: border-box;
  }
  .address-line {
    left: 666px;
    width: 460px;
    height: 3px;
    background: #000;
  }
  .address-line--1 { top: 366px; }
  .address-line--2 { top: 427px; }
  .address-line--3 { top: 488px; }
  .address-line--4 { top: 548px; }
</style>
</head>
<body>
  <main class="postcard">
    <div class="ornament ornament--header-left" role="img" aria-label="Curled scroll flourish"></div>
    <div class="ornament ornament--header-right" role="img" aria-label="Curled scroll flourish"></div>
    <h1 class="heading">SAVE <span class="heading__the">the</span> DATE</h1>
    <p class="couple">Lise &amp; Marcus</p>

    <p class="announce announce--line1">WE ARE</p>
    <p class="announce announce--line2">GETTING MARRIED</p>
    <p class="announce announce--on">ON</p>

    <div class="rule rule--left"></div>
    <div class="ornament ornament--divider" role="img" aria-label="Scrollwork divider flourish"></div>
    <div class="rule rule--right"></div>

    <p class="date">2016-12-31</p>

    <p class="about">I’m a hockey player<br>and she’s into movies...<br>we have 2 yellow labs</p>

    <div class="ornament ornament--footer" role="img" aria-label="Scrollwork footer flourish"></div>

    <div class="spine spine--top"></div>
    <div class="ornament ornament--spine" role="img" aria-label="Vertical scrollwork flourish"></div>
    <div class="spine spine--bottom"></div>

    <div class="stamp-box"></div>
    <div class="address-line address-line--1"></div>
    <div class="address-line address-line--2"></div>
    <div class="address-line address-line--3"></div>
    <div class="address-line address-line--4"></div>
  </main>
</body>
</html>
```